Basic images needed for business powerpoint slides

We need basic images for a powerpoint design. The designs should be clean, modern, simple and easy to read on a screen and if they were printed on paper. The images should not be overly designed (no fancy graphics or ornate fonts), but should still look professional.

Please pay attention to the attachments that have sketches of the images that are needed. In the notes section of the powerpoint slides specifies additional details for each image.

Also, please adhere to the design guidelines that are also uploaded. Only use colors and fonts that are specified. The final images should be similar to the look and feel of the images in the design guidelines.
Updates

Designers -
Thanks for all your submissions! I am reviewing all the designs with my team and will have a decision ready by Sunday evening. If you are submitting any new designs, please submit by Sunday morning EST so my team can review them.

Thanks!

Target Market(s)

business executives

Industry/Entity Type

Business

Requirements
Must have
• Must Have:
- 1. Please see the attached powerpoint for the sketches we would like to have recreated. There are specific notes in each slide with additional details.

2. Please refer to the following pages in the uploaded design guideline document:
Colors - p. 14
- Use either the bright or muted color options as specified in the color scheme on this page

Typography - p. 16-17
- Use either helvetica or arial options

Powerpoint guidelines - p.42
- see for example of the general look and feel of the company

```html
<!DOCTYPE html>
<html lang="en">
<head>
<meta charset="utf-8">
<title>Stakeholder Circles</title>
<link rel="stylesheet" href="https://fonts.googleapis.com/css2?family=Arimo:wght@400&display=swap">
<style>
  :root {
    --page-bg: #ffffff;
    --ring-outer: #f9eecb;
    --ring-middle: #dfe1c4;
    --ring-focus: #d47a25;
    --wedge-external: #dfcea4;
    --core: #cac89d;
    --divider: #dcdcc6;
    --label-muted: #b3ae9b;
    --label-core: #aaa78a;
    --label-strong: #111111;
  }
  html, body {
    margin: 0;
    padding: 0;
    width: 1198px;
    height: 1200px;
    overflow: hidden;
    background: var(--page-bg);
  }
  .stakeholder-map {
    display: block;
    width: 1198px;
    height: 1200px;
    font-family: "Arimo", Arial, Helvetica, sans-serif;
  }
  .ring-outer { fill: var(--ring-outer); }
  .ring-middle { fill: var(--ring-middle); }
  .ring-focus { fill: var(--ring-focus); }
  .wedge-external { fill: var(--wedge-external); }
  .core { fill: var(--core); }
  .divider { stroke: var(--divider); stroke-width: 1; }
  .tier-number { font-size: 29px; fill: var(--label-muted); }
  .tier-label { font-size: 14px; fill: var(--label-muted); }
  .core-number { font-size: 29px; fill: var(--label-core); text-anchor: middle; }
  .core-label { font-size: 14px; fill: var(--label-core); text-anchor: middle; }
  .focus-number { font-size: 30px; fill: var(--label-strong); }
  .focus-label { font-size: 14px; fill: var(--label-strong); }
  .external-label { font-size: 14px; fill: var(--label-core); text-anchor: middle; }
</style>
</head>
<body>
<svg class="stakeholder-map" viewBox="0 0 607 607" preserveAspectRatio="none" xmlns="http://www.w3.org/2000/svg">
  <circle class="ring-outer" cx="303" cy="303" r="303"/>
  <circle class="ring-middle" cx="303" cy="303" r="251"/>
  <path class="wedge-external" d="M303 303 L128.1 404 A202 202 0 0 0 477.9 404 Z"/>
  <path class="ring-focus" d="M128.1 404 A202 202 0 1 1 477.9 404 L445.9 385.5 A165 165 0 1 0 160.1 385.5 Z"/>
  <circle class="core" cx="303" cy="303" r="165"/>
  <line class="divider" x1="303" y1="303" x2="303" y2="138"/>
  <line class="divider" x1="303" y1="303" x2="160.1" y2="385.5"/>
  <line class="divider" x1="303" y1="303" x2="445.9" y2="385.5"/>

  <g class="tier tier-15">
    <text class="tier-number" x="176" y="51">15</text>
    <text class="tier-label" x="298" y="22" text-anchor="middle">Franchise Lawyers</text>
    <text class="tier-label" x="298" y="35" text-anchor="middle">Finance</text>
    <text class="tier-label" x="302" y="48" text-anchor="middle">Committee Members</text>
  </g>

  <g class="tier tier-14">
    <text class="tier-number" x="208" y="97">14</text>
    <text class="tier-label" x="250" y="86">Legal Analysts</text>
  </g>

  <g class="tier tier-13">
    <text class="focus-number" x="218" y="147">13</text>
    <text class="focus-label" x="264" y="119">Physicians,</text>
    <text class="focus-label" x="264" y="132">Clinicians,</text>
    <text class="focus-label" x="264" y="146">Scientists</text>
  </g>

  <g class="tier tier-10">
    <text class="core-number" x="238" y="230">10</text>
    <text class="core-label" x="234" y="257">HFAC Specialists</text>
    <text class="core-label" x="234" y="274">(Med Products-</text>
    <text class="core-label" x="234" y="291">Med Affairs)</text>
  </g>

  <g class="tier tier-11">
    <text class="core-number" x="364" y="230">11</text>
    <text class="core-label" x="374" y="257">HFAC Specialists</text>
    <text class="core-label" x="374" y="274">(Bio Science-</text>
    <text class="core-label" x="374" y="291">Med Affairs)</text>
  </g>

  <g class="tier tier-12">
    <text class="core-number" x="305" y="372">12</text>
    <text class="core-label" x="305" y="391">HFAC Specialists</text>
    <text class="core-label" x="305" y="409">(Contributions Management</text>
    <text class="core-label" x="305" y="426">Program)</text>
  </g>

  <text class="external-label" x="305" y="481">External Orgs</text>
</svg>
</body>
</html>
```